Virtual Restaurant Menu Design

I need a menu displayed on monitors of my casual restaurant. I currently have 3 monitors, I could potentially add 2 more. My menu is quite large but I need the monitors to each display part of the menu in a manner that is visually appealing but still easy to read. That means there needs to be 3 separate files where one file will be displayed on one monitor and the other two files on the the other monitors. Looking for a classic and clean look. I have attached menu for reference. Including some professional pictures incase you can incorporate them into the design for that section. Catering and beverage section of menu need not be displayed. I would like an editable version of this incase my prices change in the future.Good performance on this will very likely lead to future work as I have specials that I like to change and display on a monthly basis.
Italian Restaurant

```html
<!DOCTYPE html>
<html lang="en">
<head>
<meta charset="utf-8">
<title>Bellavia Kitchen – Menu Board</title>
<link href="https://fonts.googleapis.com/css2?family=Archivo:ital,wght@0,400;0,500;0,600;0,700;1,400&display=swap" rel="stylesheet">
<style>
:root{
  --backdrop:#efeff1;
  --paper:#f7f4e3;
  --rule:#6b5a4a;
  --band:#f7941d;
  --accent:#f26522;
  --green:#1a6b2d;
  --red:#d2232a;
  --teal:#00a99d;
  --ink:#2b2b2b;
  --white:#ffffff;
}
*{box-sizing:border-box;margin:0;padding:0}
html,body{width:1200px;height:923px;overflow:hidden;background:var(--backdrop)}
body{font-family:"Archivo",Arial,sans-serif;color:var(--ink)}
.stage{width:1300px;height:1000px;transform:scale(.923077);transform-origin:0 0;position:relative}
.board{position:absolute;left:8px;top:140px;width:1283px;height:720px;background:var(--paper);box-shadow:0 6px 14px rgba(0,0,0,.28)}
.panel{position:absolute;border:1px solid var(--rule)}
.panel--left{left:19px;top:18px;width:408px;height:684px}
.panel--right{left:857px;top:18px;width:409px;height:684px}
.panel--photos{left:438px;top:275px;width:408px;height:427px}
.blk{position:absolute;left:9px;width:388px;text-align:center}
.panel--right .blk{left:9px;width:389px}
.band{height:33px;background:var(--band);font-size:26px;font-weight:600;letter-spacing:1px;line-height:34px;color:var(--ink)}
.card{background:var(--white);border-radius:6px}
.featured{border:2px dotted var(--band);box-shadow:0 0 0 2px var(--white),0 0 0 4px rgba(210,35,42,.35);border-radius:8px}
.item{color:var(--accent);font-weight:600;font-size:16.5px;line-height:20px}
.desc{font-style:italic;font-size:12.5px;line-height:14px;color:var(--ink)}
.prices{font-size:17px;font-weight:600;color:var(--green);display:flex;justify-content:center;gap:18px}
.prices b{font-weight:500;color:var(--ink);font-size:14px;margin-left:14px;align-self:center}
.extras{font-size:10px;color:var(--red);font-weight:500}
.extras b{color:var(--ink);font-weight:500;font-size:9px;margin:0 4px}
.feat-title{display:flex;align-items:center;justify-content:center;gap:8px;font-size:17px;font-weight:600;color:var(--ink)}
.stars{display:inline-flex;gap:3px}
.stars svg{width:13px;height:13px;fill:var(--band)}
.flag{width:18px;height:13px}
.brand{position:absolute;left:438px;top:118px;width:408px;display:flex;align-items:center;justify-content:center;gap:12px}
.brand-mark{width:20px;height:20px;border-radius:50%;background:var(--teal);flex:none}
.brand-name{font-size:38px;font-weight:600;color:var(--teal);letter-spacing:.5px}
.tagline{position:absolute;left:438px;top:238px;width:408px;text-align:center;font-size:17px;font-weight:500;color:#111}
.photo{position:absolute;left:8px;width:392px;border:2px dotted var(--band);padding:2px}
.photo-fill{width:100%;height:100%}
.photo-steak .photo-fill{background:linear-gradient(135deg,#6f6e6c,#c9a46a 45%,#8a5a30 70%,#4b4a48)}
.photo-cannoli .photo-fill{background:linear-gradient(135deg,#3b3b3b,#d9d9d9 45%,#5a3a22 60%,#cfcfcf)}
.caption{position:absolute;right:22px;bottom:12px;color:var(--white);font-style:italic;font-size:16px}
.dessert-row{position:absolute;left:50px;width:341px;display:flex;justify-content:space-between;align-items:baseline}
.dessert-row .item{font-size:16px}
.dessert-row .price{font-style:italic;font-size:13px}
</style>
</head>
<body>
<svg width="0" height="0" style="position:absolute">
  <symbol id="star" viewBox="0 0 24 24"><path d="M12 1.5l3.2 6.9 7.5.8-5.6 5.1 1.6 7.4L12 17.9l-6.7 3.8 1.6-7.4L1.3 9.2l7.5-.8z"/></symbol>
  <symbol id="flag" viewBox="0 0 18 13"><rect width="6" height="13" fill="#1e9e4a"/><rect x="6" width="6" height="13" fill="#fff"/><rect x="12" width="6" height="13" fill="#e0252b"/></symbol>
</svg>
<div class="stage">
 <div class="board">

  <section class="panel panel--left">
    <h2 class="blk band" style="top:9px">DELI SUBS</h2>
    <div class="blk prices" style="top:51px"><span>Whole Subs<b>8.50</b></span><span>Half Subs<b>5.50</b></span></div>
    <p class="blk desc" style="top:72px">Served with lettuce, tomatoes, onions, hot peppers &amp;<br>mayo unless other specified</p>
    <p class="blk extras" style="top:104px">Extra Meat<b>2.50</b> • Extra Cheese<b>1.50</b> • Extra Toppings<b>.50 each</b></p>
    <div class="blk card featured" style="top:128px;height:71px;padding-top:10px">
      <div class="feat-title">
        <span class="stars"><svg><use href="#star"/></svg><svg><use href="#star"/></svg><svg><use href="#star"/></svg><svg><use href="#star"/></svg></span>
        <svg class="flag" style="margin-left:14px"><use href="#flag"/></svg>Steak &amp; Cheese
        <span class="stars" style="margin-left:36px"><svg><use href="#star"/></svg><svg><use href="#star"/></svg><svg><use href="#star"/></svg><svg><use href="#star"/></svg></span>
      </div>
      <p class="desc" style="margin-top:4px">High Quality Philly style steak grilled with onions.<br>A customer favorite!</p>
    </div>
    <div class="blk card" style="top:209px;height:30px;padding-top:5px"><p class="item">Chicken Steak</p></div>
    <div class="blk" style="top:243px"><p class="item">Prosciutto &amp; Mozzarella</p><p class="desc" style="margin-top:2px">[ Hot or Cold ] Served with Italian dressing</p></div>
    <div class="blk card" style="top:285px;height:47px;padding-top:4px"><p class="item">Ham &amp; Steak</p><p class="desc" style="margin-top:2px">[ Hot or Cold ] Served with Italian dressing</p></div>
    <div class="blk" style="top:338px"><p class="item">Turkey &amp; Cheese</p><p class="desc" style="margin-top:2px">[ Hot or Cold ] Served with Italian dressing</p></div>
    <div class="blk card" style="top:382px;height:48px;padding-top:4px"><p class="item">Italian Hoagie</p><p class="desc" style="margin-top:3px">[ Hot or Cold ] Salami, ham, cheese&amp; italian dressing</p></div>
    <h2 class="blk band" style="top:443px">GOURMET SOUPS</h2>
    <div class="blk prices" style="top:481px"><span>Whole Subs<b>8.95</b></span><span>Half Subs<b>5.90</b></span></div>
    <p class="blk extras" style="top:500px">Extra Meat<b>2.50</b> • Extra Cheese<b>1.50</b> • Extra Toppings<b>.50 each</b></p>
    <div class="blk card" style="top:518px;height:55px;padding-top:3px"><p class="item">Parmigiana</p><p class="desc" style="margin-top:2px">Meatball, Chicken or Eggplant with tomato sauce &amp;<br>mozzarella</p></div>
    <div class="blk" style="top:578px"><p class="item">Caprese Sandwich</p><p class="desc" style="margin-top:2px">[ Hot or Cold ] Fresh Tomatoes &amp; mozzarella drizlled<br>with olive oil , topped with basil</p></div>
    <div class="blk card" style="top:631px;height:41px;padding-top:3px;left:12px;width:386px"><p class="item">Veal Parmigiana</p><p class="desc">Tomato sauce &amp; mozzarella</p></div>
  </section>

  <header class="brand">
    <span class="brand-mark"></span>
    <h1 class="brand-name">Bellavia Kitchen</h1>
  </header>
  <p class="tagline">Autenthic Italian Cuisine &amp; Pizza</p>

  <section class="panel panel--photos">
    <figure class="photo photo-steak" style="top:8px;height:200px">
      <div class="photo-fill" role="img" aria-label="Photo of a steak and cheese sub topped with tomato slices and peppers"></div>
      <figcaption class="caption">Steak &amp; Cheese</figcaption>
    </figure>
    <figure class="photo photo-cannoli" style="top:215px;height:203px">
      <div class="photo-fill" role="img" aria-label="Photo of a chocolate-dipped Italian cannoli dusted with powdered sugar on a white plate"></div>
      <figcaption class="caption">Italian Cannoli</figcaption>
    </figure>
  </section>

  <section class="panel panel--right">
    <div class="blk" style="top:11px"><p class="item">Grilled Italian Sausage</p><p class="desc" style="margin-top:2px">Peppers, onions &amp; cheese</p></div>
    <div class="blk card" style="top:53px;height:47px;padding-top:4px"><p class="item">Veggie Subs</p><p class="desc" style="margin-top:5px">Seasonal vegetables, please inquire</p></div>
    <h2 class="blk band" style="top:113px">Kids Menu</h2>
    <p class="blk desc" style="top:152px">All items on the menu are availabel for kids, please<br>ask your server!</p>
    <div class="blk card" style="top:189px;height:47px;padding-top:3px"><p class="item">Chicken Tenders</p><p class="desc" style="margin-top:3px">With french fries &nbsp;&nbsp;6.25</p></div>
    <div class="blk" style="top:242px"><p class="item">Kids Spaghetti or Penne</p><p class="desc" style="margin-top:2px">With choice of tomato sauce, meat sauce, meat ball<br>or alfredo sauce &nbsp;&nbsp;6.75</p></div>
    <div class="blk card" style="top:297px;height:47px;padding-top:4px"><p class="item">Cheese Tortellini</p><p class="desc" style="margin-top:7px">6.75</p></div>
    <div class="blk" style="top:351px"><p class="item">Italian Macaroni &amp; Cheese</p><p class="desc" style="margin-top:5px">6.75</p></div>
    <div class="blk card" style="top:395px;height:58px;padding-top:3px"><p class="item">Drinks</p><p class="desc" style="margin-top:3px">Milk, chocolate milk, juice, small bottled water or<br>soda &nbsp;&nbsp;1.50</p></div>
    <h2 class="blk band" style="top:466px">Dessert</h2>
    <div class="blk card featured" style="top:508px;height:38px;display:flex;align-items:center;padding:0 10px">
      <svg class="flag"><use href="#flag"/></svg>
      <span style="font-size:16px;font-weight:500;margin:0 10px 0 8px">Italian Cannoli</span>
      <span class="stars"><svg><use href="#star"/></svg><svg><use href="#star"/></svg><svg><use href="#star"/></svg><svg><use href="#star"/></svg></span>
      <span class="desc" style="margin-left:auto;font-size:13px">2.95</span>
    </div>
    <div class="dessert-row" style="top:553px"><span class="item">Tiramisu</span><span class="price">4.95</span></div>
    <div class="dessert-row" style="top:578px"><span class="item">Cheesecake</span><span class="price">4.95</span></div>
    <div class="dessert-row" style="top:603px"><span class="item">Sfogliatela</span><span class="price">1.75</span></div>
    <div class="dessert-row" style="top:628px"><span class="item">Chocolate Mouse Cup</span><span class="price">4.95</span></div>
    <div class="dessert-row" style="top:653px"><span class="item">Gelato Italiano</span><span class="price">sm 3.95 reg 4.95</span></div>
  </section>

 </div>
</div>
</body>
</html>
```